International Lifestyle Real Estate Brokerage Needs Eye Catching Website

We need a new website for a cutting edge / dynamic real estate startup, Pinecrest Realty, that will serve as a concierge brokerage to assist cold weather residents with the research, selection, financing and purchase of vacation / retirement properties in warm weather climates in the US and then globally. We will have personally vetted all properties to insure that our clients are only getting the best of the best with no hidden surprises.

** The website design will ultimately need to be coded into a wordpress theme.

We are not locked into any specific colour scheme but would prefer something warm vs cold as that is really the lifestyle we are selling. We like lots of white negative space and hope to allow high end photography to provide most of the pop in colour.

I have attached mock up wire frames to demonstrate desired functionality for three pages we need designed

1) Home Page
2) Market Profile (City overview and developments)
3) Community Profile Page (Individual development profile)

I have also included .ai file for the logo. Not locked into red.

Final design should communicate excitement, lifestyle while maintaining an air of professionalism and reliability. We have developed over 30 sites and have high expectations for the winning design.

Regards,
Dan
Updates

Project Deadline Extended Reason: Hello,I have been called away from this project for the past couple of weeks and have been unable to get together with the people involved to get a consensus on direction forward. Apologies for the delay - we are still very much committed to moving forward.Regards,Dan Added Wednesday, July 6, 2016

Target Market(s)

Canadian and Northern US residents looking to purchase vacation or retirement real estate in warmer climates, initially in the US, but eventually Internationally.

Industry/Entity Type

Real Estate

Contact Information for Business Card

Names for Business Cards

Dan Whitford
705.555.2147
dan@pinecrestrealty-example.ca

Coding

Coded - Design and coding required

Number of Pages Required

3 page

Font styles to use
Serif
Sans Serif

Requirements
Must have
• See wireframe documents uploaded.
• Site design will ultimately be coded into a child theme to function on a selected wordpress theme. If the designer has a Wordpres Theme in mind that would be compatible with the design we would appreciate that information.
Nice to have
• See wireframe documents uploaded. Prefer clean, modern site, white negative space, bold photography will add most of the colour and pop.
Should not have
• Anything cartoony or sophmoric.

```html
<!DOCTYPE html>
<html lang="en">
<head>
<meta charset="utf-8">
<title>Pinecrest Realty — Warm Weather Living</title>
<link href="https://fonts.googleapis.com/css2?family=Oswald:wght@400;500&family=Lato:wght@400;700&display=swap" rel="stylesheet">
<style>
:root{
  --red:#d6202a;
  --red-dark:#b3151e;
  --ink:#222222;
  --ink-soft:#555555;
  --white:#ffffff;
  --paper:#f3f3f3;
  --paper-2:#e9e9e9;
  --night:#1c1f24;
  --footer:#1b1b1b;
  --line:#d9d9d9;
}
*{box-sizing:border-box;margin:0;padding:0}
html,body{width:1200px;height:3495px;overflow:hidden}
body{font-family:"Lato",Arial,sans-serif;color:var(--ink);background:var(--white);position:relative}
.abs{position:absolute}
.heading{font-family:"Oswald",Arial,sans-serif;font-weight:400;text-transform:uppercase;text-align:center;font-size:34px;letter-spacing:.5px}
.heading-rule{position:absolute;left:50%;transform:translateX(-50%);width:380px;height:14px}
.heading-rule::before,.heading-rule::after{content:"";position:absolute;top:6px;width:170px;height:1px;background:var(--line)}
.heading-rule::before{left:0}.heading-rule::after{right:0}
.heading-rule i{position:absolute;left:50%;top:3px;width:8px;height:8px;margin-left:-4px;background:var(--red);border-radius:50%}

/* header */
.site-header{left:0;top:0;width:1200px;height:145px;background:var(--white)}
.brand{left:98px;top:28px;display:flex;align-items:center;gap:12px}
.brand-dot{width:22px;height:22px;background:var(--red);border-radius:50%}
.brand-name{font-family:"Oswald",sans-serif;font-size:30px;color:var(--red);letter-spacing:2px;text-transform:uppercase;line-height:1}
.header-phone{left:618px;top:38px;display:flex;align-items:center;gap:8px;font-family:"Oswald",sans-serif;font-size:20px}
.header-actions{left:782px;top:34px;display:flex;gap:12px}
.header-btn{height:34px;background:var(--ink);color:var(--white);font-family:"Oswald",sans-serif;font-size:15px;display:flex;align-items:center;padding-left:12px;text-transform:uppercase}
.header-btn span.tag{width:32px;height:34px;background:var(--red);margin-left:10px;display:flex;align-items:center;justify-content:center}
.main-nav{left:368px;top:100px;display:flex;font-family:"Oswald",sans-serif;font-size:16px;text-transform:uppercase}
.main-nav a{color:var(--ink);text-decoration:none;height:42px;display:flex;align-items:center;padding:0 28px}
.main-nav a.active{background:var(--red);color:var(--white);clip-path:polygon(0 0,88% 0,100% 100%,0 100%)}
.nav-rule{left:368px;top:142px;width:732px;height:3px;background:var(--red)}

/* hero */
.hero{left:0;top:145px;width:1200px;height:505px;background:linear-gradient(180deg,#5d9ad6 0%,#a8c9e6 35%,#c79a62 60%,#6a7a3a 85%,#3c6fa0 100%)}
.hero-arrow{top:378px;width:40px;height:32px;background:rgba(0,0,0,.55);display:flex;align-items:center;justify-content:center}
.hero-title{left:0;top:530px;width:1200px;text-align:center;font-family:"Oswald",sans-serif;font-size:38px;color:var(--white);text-shadow:0 2px 6px rgba(0,0,0,.6)}
.hero-sub{left:0;top:583px;width:1200px;text-align:center;font-size:23px;color:var(--white);text-shadow:0 2px 6px rgba(0,0,0,.6)}

/* services */
.services{left:0;top:650px;width:1200px;height:470px;background:linear-gradient(180deg,#2a2e34,#15171b)}
.services .heading{color:var(--white)}
.services-intro{left:0;top:785px;width:1200px;text-align:center;color:#e5e5e5;font-size:15px}
.service{top:840px;width:200px;text-align:center}
.service-icon{width:104px;height:104px;margin:0 auto;border-radius:50%;background:var(--white);border:4px solid var(--red);display:flex;align-items:center;justify-content:center}
.service-label{margin-top:18px;color:var(--white);font-family:"Oswald",sans-serif;font-size:22px}
.btn-red{background:var(--red);color:var(--white);font-family:"Oswald",sans-serif;text-transform:uppercase;display:flex;align-items:center;justify-content:center}

/* developments */
.developments{left:0;top:1120px;width:1200px;height:680px;background:var(--paper)}
.dev-photo{left:100px;top:1255px;width:1000px;height:385px;background:linear-gradient(180deg,#2f4a6b 0%,#e8e8e4 40%,#8a7a5a 65%,#2b8fc0 85%,#1f6f9a 100%)}
.dev-caption{left:100px;top:1604px;width:1000px;height:36px;background:rgba(214,32,42,.9);color:var(--white);text-align:center;font-size:17px;font-weight:700;line-height:36px}
.dev-strip{left:100px;top:1645px;width:1000px;height:95px;background:#2a2a2a;display:flex;gap:8px;padding:8px 10px}
.dev-thumb{flex:1;height:79px}
.strip-arrow{top:1678px;width:28px;height:28px;border-radius:50%;background:#2a2a2a;display:flex;align-items:center;justify-content:center}

/* markets */
.markets{left:0;top:1800px;width:1200px;height:670px;background:var(--paper-2)}
.market-tabs{left:380px;top:1940px;display:flex;gap:4px;font-family:"Oswald",sans-serif;font-size:18px;text-transform:uppercase}
.market-tabs span{background:#111;color:var(--white);height:44px;display:flex;align-items:center;padding:0 20px}
.market-tabs span.active{background:var(--red)}
.market-tile{width:326px;height:198px}
.market-name{position:absolute;left:0;bottom:0;width:100%;height:32px;background:rgba(0,0,0,.6);color:var(--white);text-align:center;font-size:16px;line-height:32px;text-transform:uppercase}
.commitment{background:linear-gradient(135deg,#2b3c55,#4a5c78);color:var(--white);text-align:center;padding:40px 22px}
.commitment h3{font-family:"Oswald",sans-serif;font-weight:400;font-size:18px;margin-bottom:10px}
.commitment p{font-size:14px;line-height:1.45}

/* blog */
.blog{left:0;top:2470px;width:1200px;height:425px;background:var(--white)}
.post{top:2615px;width:487px;height:230px;border:1px solid var(--line);background:var(--white)}
.post-photo{position:absolute;left:6px;top:6px;width:205px;height:218px}
.post-body{position:absolute;left:232px;top:18px;width:240px}
.post-body h4{font-family:"Oswald",sans-serif;font-weight:400;font-size:16px;text-transform:uppercase}
.post-date{color:var(--red);font-size:13px;margin:12px 0 8px}
.post-body p{font-size:12.5px;line-height:1.55;color:var(--ink-soft)}
.post-body p b{color:var(--red);font-weight:400}

/* callback */
.callback{left:0;top:2895px;width:1200px;height:280px;background:linear-gradient(180deg,#4f5358,#3a3d42)}
.callback-title{left:100px;top:2930px;font-family:"Oswald",sans-serif;font-size:40px;line-height:1.15;color:var(--white)}
.callback-text{left:100px;top:3040px;width:290px;font-size:13px;line-height:1.5;color:#e2e2e2}
.form-label{left:460px;top:2940px;color:var(--white);font-size:14px;font-weight:700}
.field{height:42px;background:var(--white);color:#888;font-size:12px;padding:0 12px;display:flex;align-items:center}
.submit{left:460px;top:3078px;width:162px;height:44px;font-size:20px}

/* footer */
.footer{left:0;top:3175px;width:1200px;height:275px;background:var(--footer);color:#ddd}
.footer-title{font-family:"Oswald",sans-serif;font-size:15px;color:var(--white);text-transform:uppercase}
.footer-title::after{content:"";display:block;width:42px;height:2px;background:var(--red);margin-top:8px}
.footer-links{list-style:none;font-size:14px;line-height:24.5px}
.footer-links li::before{content:"› ";color:var(--red)}
.contact-row{display:flex;gap:10px;font-size:13px;line-height:1.35;margin-bottom:14px}
.map{left:610px;top:3265px;width:228px;height:132px;background:linear-gradient(135deg,#d8e3c9,#aecbe6);border:3px solid var(--white)}
.footer-brand{left:920px;top:3320px;display:flex;align-items:center;gap:12px}
.copyright-bar{left:0;top:3450px;width:1200px;height:45px;background:var(--red);color:var(--white);font-size:13px;font-weight:700}
.social{display:flex;gap:10px}
.social span{width:30px;height:30px;border-radius:50%;border:2px solid var(--white)}
</style>
</head>
<body>

<header class="site-header abs">
  <div class="brand abs"><div class="brand-dot"></div><div class="brand-name">Pinecrest Realty</div></div>
  <div class="header-phone abs">
    <svg width="20" height="20" viewBox="0 0 24 24"><path d="M6.6 10.8a15 15 0 006.6 6.6l2.2-2.2c.3-.3.7-.4 1-.2 1.1.4 2.3.6 3.6.6.6 0 1 .4 1 1V20c0 .6-.4 1-1 1A17 17 0 013 4c0-.6.4-1 1-1h3.5c.6 0 1 .4 1 1 0 1.3.2 2.5.6 3.6.1.3 0 .7-.2 1z" fill="#222"/></svg>
    123-456-7890
  </div>
  <div class="header-actions abs">
    <div class="header-btn">Search<span class="tag"><svg width="16" height="16" viewBox="0 0 16 16"><circle cx="6.5" cy="6.5" r="4.5" stroke="#fff" stroke-width="2" fill="none"/><path d="M10 10l4 4" stroke="#fff" stroke-width="2"/></svg></span></div>
    <div class="header-btn">Login<span class="tag"><svg width="16" height="16" viewBox="0 0 16 16"><path d="M2 8h8M7 5l3 3-3 3M10 2h4v12h-4" stroke="#fff" stroke-width="2" fill="none"/></svg></span></div>
    <div class="header-btn">Register<span class="tag"><svg width="16" height="16" viewBox="0 0 16 16"><path d="M3 13l1-4 7-7 3 3-7 7z" stroke="#fff" stroke-width="1.8" fill="none"/></svg></span></div>
  </div>
  <nav class="main-nav abs">
    <a class="active" href="#">Home</a><a href="#">About</a><a href="#">Saved</a><a href="#">Our Process</a><a href="#">Resources</a><a href="#">Contact</a>
  </nav>
  <div class="nav-rule abs"></div>
</header>

<section class="hero abs" role="img" aria-label="Sunny stucco house with terrace, garden and pool under a blue sky"></section>
<div class="hero-arrow abs" style="left:0"><svg width="12" height="14" viewBox="0 0 12 14"><path d="M9 1L3 7l6 6" stroke="#fff" stroke-width="2.5" fill="none"/></svg></div>
<div class="hero-arrow abs" style="left:1160px"><svg width="12" height="14" viewBox="0 0 12 14"><path d="M3 1l6 6-6 6" stroke="#fff" stroke-width="2.5" fill="none"/></svg></div>
<div class="hero-title abs">LIFE IS TOO SHORT TO BE COLD</div>
<div class="hero-sub abs">Where do you want to play in sunshine</div>

<section class="services abs" aria-label="Services"></section>
<h2 class="heading abs" style="left:0;top:684px;width:1200px;color:#fff">Services We Provide</h2>
<div class="heading-rule abs" style="top:740px"><i></i></div>
<p class="services-intro abs">Lorem ipsum dolor sit amet, consectetuer adipiscing elit, sed diam nonummy nibh euismod tincidunt ut laoreet dolore magna aliquam erat volutpat.</p>
<div class="service abs" style="left:125px"><div class="service-icon"><svg width="50" height="50" viewBox="0 0 50 50"><path d="M8 24L25 10l17 14M13 20v20h24V20" stroke="#222" stroke-width="3" fill="none"/><circle cx="25" cy="30" r="5" fill="#d6202a"/></svg></div><div class="service-label">For Buyers</div></div>
<div class="service abs" style="left:360px"><div class="service-icon"><svg width="50" height="50" viewBox="0 0 50 50"><path d="M8 24L25 10l17 14M13 20v20h24V20" stroke="#222" stroke-width="3" fill="none"/><text x="25" y="37" font-family="Oswald" font-size="15" text-anchor="middle" fill="#d6202a">$</text></svg></div><div class="service-label">For Sellers</div></div>
<div class="service abs" style="left:595px"><div class="service-icon"><svg width="50" height="50" viewBox="0 0 50 50"><path d="M12 42V10h22M12 16h28M30 16v10" stroke="#222" stroke-width="3" fill="none"/><rect x="22" y="30" width="16" height="12" fill="#d6202a"/></svg></div><div class="service-label">Developments</div></div>
<div class="service abs" style="left:830px"><div class="service-icon"><svg width="50" height="50" viewBox="0 0 50 50"><path d="M8 24L25 10l17 14M13 20v20h14" stroke="#222" stroke-width="3" fill="none"/><circle cx="32" cy="30" r="6" stroke="#d6202a" stroke-width="3" fill="none"/><path d="M36 34l6 6" stroke="#d6202a" stroke-width="3"/></svg></div><div class="service-label">Property Survey</div></div>
<div class="btn-red abs" style="left:508px;top:1027px;width:185px;height:48px;font-size:21px">Learn More</div>

<section class="developments abs" aria-label="Featured developments"></section>
<h2 class="heading abs" style="left:0;top:1157px;width:1200px">Featured Developments</h2>
<div class="heading-rule abs" style="top:1210px"><i></i></div>
<div class="dev-photo abs" role="img" aria-label="Modern white villa with lit interior, lounge terrace and long pool at dusk"></div>
<div class="dev-caption abs">Lorem ipsum dolor sit amet, consectetuer</div>
<div class="dev-strip abs">
  <div class="dev-thumb" role="img" aria-label="Living room interior" style="background:linear-gradient(135deg,#cfc7b8,#8a7a62)"></div>
  <div class="dev-thumb" role="img" aria-label="House exterior with lawn" style="background:linear-gradient(135deg,#8fb0cf,#6e8a4a)"></div>
  <div class="dev-thumb" role="img" aria-label="Pool at a resort" style="background:linear-gradient(135deg,#4d86b8,#2f9fcf)"></div>
  <div class="dev-thumb" role="img" aria-label="Villa at night" style="background:linear-gradient(135deg,#2a3550,#c9954a)"></div>
  <div class="dev-thumb" role="img" aria-label="Bright open plan room" style="background:linear-gradient(135deg,#e6e2da,#a99c86)"></div>
  <div class="dev-thumb" role="img" aria-label="Bedroom interior" style="background:linear-gradient(135deg,#d9d4cc,#7d6f5e)"></div>
</div>
<div class="strip-arrow abs" style="left:84px"><svg width="10" height="12" viewBox="0 0 10 12"><path d="M7 1L2 6l5 5" stroke="#fff" stroke-width="2" fill="none"/></svg></div>
<div class="strip-arrow abs" style="left:1088px"><svg width="10" height="12" viewBox="0 0 10 12"><path d="M3 1l5 5-5 5" stroke="#fff" stroke-width="2" fill="none"/></svg></div>

<section class="markets abs" aria-label="Featured markets"></section>
<h2 class="heading abs" style="left:0;top:1835px;width:1200px">Featured Markets</h2>
<div class="heading-rule abs" style="top:1890px"><i></i></div>
<div class="market-tabs abs"><span class="active">United States</span><span>Mexico</span><span>South America</span></div>
<div class="market-tile abs" style="left:100px;top:2020px;background:linear-gradient(160deg,#3d5a86,#c08a4a)" role="img" aria-label="Modern Orlando home at dusk"><div class="market-name">Orlando</div></div>
<div class="market-tile abs" style="left:437px;top:2020px;background:linear-gradient(160deg,#2f5fa8,#d07a9a)" role="img" aria-label="Naples pool terrace with palm trees"><div class="market-name">Naples</div></div>
<div class="market-tile abs" style="left:774px;top:2020px;background:linear-gradient(160deg,#3a3430,#9a8066)" role="img" aria-label="Fort Myers kitchen interior"><div class="market-name">Fort Meyers</div></div>
<div class="market-tile abs" style="left:100px;top:2230px;background:linear-gradient(160deg,#1c2b52,#c9924e)" role="img" aria-label="Clearwater home lit at night"><div class="market-name">Clearwater</div></div>
<div class="market-tile abs" style="left:437px;top:2230px;background:linear-gradient(160deg,#2a2f6a,#9aa0d8)" role="img" aria-label="Asheville modern interior"><div class="market-name">Asheville</div></div>
<div class="market-tile abs commitment" style="left:774px;top:2230px"><h3>OUR COMMITMENT</h3><p>Lorem ipsum dolor sit amet, consectetuer adipiscing elit sed diam nibh euismod tincidunt ut laoreet dolore magna aliquam erat volutpat nulla.</p></div>

<section class="blog abs" aria-label="Recent blog posts"></section>
<h2 class="heading abs" style="left:0;top:2505px;width:1200px">Recent Blog Posts</h2>
<div class="heading-rule abs" style="top:2560px"><i></i></div>
<article class="post abs" style="left:100px">
  <div class="post-photo" role="img" aria-label="Two storey suburban home with garage" style="background:linear-gradient(180deg,#5a8fcf,#c9c2b0 60%,#5f8a3e)"></div>
  <div class="post-body"><h4>Ut tellus dolor dapibus dolor</h4><div class="post-date">22.06.2016</div><p>Duis autem vel eum iriure dolor in hendrerit in vulputate velit esse molestie consequat, vel illum dolore eu feugiat nulla facilisis at vero eros et accumsan et iusto odio dignissim qui blandit praesent luptatum zzril delenit augue duis dolore te feugait nulla facilisi. <b>[+]</b></p></div>
</article>
<article class="post abs" style="left:613px">
  <div class="post-photo" role="img" aria-label="Beige villa with balconies and palms" style="background:linear-gradient(180deg,#8fb4d8,#d8c29a 55%,#6b7f45)"></div>
  <div class="post-body"><h4>Ut tellus dolor almet sit dolor</h4><div class="post-date">22.06.2016</div><p>Duis autem vel eum iriure dolor in hendrerit in vulputate velit esse molestie consequat, vel illum dolore eu feugiat nulla facilisis at vero eros et accumsan et iusto odio dignissim qui blandit praesent luptatum zzril delenit augue duis dolore te feugait nulla facilisi. <b>[+]</b></p></div>
</article>

<section class="callback abs" role="img" aria-label="Dimmed photo of a home behind the call back form"></section>
<div class="callback-title abs">Request<br>A Call Back.</div>
<p class="callback-text abs">Duis autem vel eum iriure dolor in hendrerit in vulputate velit esse molestie consequat, vel illum dolore eu feugiat nulla facilisis at vero.</p>
<div class="form-label abs">Please fill up below form</div>
<div class="field abs" style="left:460px;top:2968px;width:306px">Name</div>
<div class="field abs" style="left:794px;top:2968px;width:306px">Email</div>
<div class="field abs" style="left:460px;top:3020px;width:306px">Phone</div>
<div class="field abs" style="left:794px;top:3020px;width:306px">Message</div>
<div class="btn-red submit abs">Submit</div>

<footer class="footer abs"></footer>
<div class="abs" style="left:100px;top:3222px"><div class="footer-title">Quick Links</div>
  <ul class="footer-links" style="margin-top:14px"><li>Home</li><li>About</li><li>Saved</li><li>Our Process</li><li>Resources</li><li>Contact</li></ul></div>
<div class="abs" style="left:300px;top:3222px;width:240px"><div class="footer-title" style="margin-bottom:16px">Contact Details</div>
  <div class="contact-row"><svg width="14" height="18" viewBox="0 0 14 18"><path d="M7 0a7 7 0 00-7 7c0 5 7 11 7 11s7-6 7-11a7 7 0 00-7-7z" fill="#d6202a"/><circle cx="7" cy="7" r="2.5" fill="#1b1b1b"/></svg><div><b>Pinecrest Realty</b><br>123 PG Duis aute irure dolor<br>reprehenderit in voluptate</div></div>
  <div class="contact-row"><svg width="16" height="16" viewBox="0 0 24 24"><path d="M6.6 10.8a15 15 0 006.6 6.6l2.2-2.2c.3-.3.7-.4 1-.2 1.1.4 2.3.6 3.6.6.6 0 1 .4 1 1V20c0 .6-.4 1-1 1A17 17 0 013 4c0-.6.4-1 1-1h3.5c.6 0 1 .4 1 1 0 1.3.2 2.5.6 3.6.1.3 0 .7-.2 1z" fill="#d6202a"/></svg>+ (123) 456 7890</div>
  <div class="contact-row"><svg width="16" height="16" viewBox="0 0 16 16"><rect x="1" y="5" width="14" height="9" fill="#d6202a"/><rect x="4" y="1" width="8" height="5" fill="none" stroke="#d6202a" stroke-width="1.5"/></svg>+ (123) 456 7890</div>
  <div class="contact-row"><svg width="16" height="14" viewBox="0 0 16 14"><rect x="1" y="2" width="14" height="10" fill="none" stroke="#d6202a" stroke-width="1.5"/><path d="M1 2l7 6 7-6" stroke="#d6202a" stroke-width="1.5" fill="none"/></svg>info@pinecrestrealty-example.com</div></div>
<div class="abs" style="left:610px;top:3222px"><div class="footer-title">Location Map</div></div>
<div class="map abs" role="img" aria-label="Street map showing the office location"></div>
<div class="footer-brand abs"><div class="brand-dot" style="background:#cfcfcf"></div><div class="brand-name" style="color:#cfcfcf;font-size:24px">Pinecrest Realty</div></div>

<div class="copyright-bar abs">
  <div class="abs" style="left:100px;top:14px">Copyright © 2016 Pinecrest Realty. All Rights Reserved.</div>
  <div class="social abs" style="left:950px;top:7px"><span></span><span></span><span></span><span></span></div>
</div>

</body>
</html>
```